Kitchen and custom cabinetry company looking for business card design

We make: * Custom Kitchens, contemporary and traditional kitchens, Vanities, Libraries, Custom Entry Doors, Custom Wine Cellars and Custom Design Furniture. Phone number 555-318-2746. Address: Westhampton NY. Email: BRAVOK@mailbox.example Portfolio at: BRAVOKcabinetry.example I would like moderns fonts and not heavy lines. double side but maybe will use clear plastic. I attached the logo.

```html
<!DOCTYPE html>
<html lang="en">
<head>
<meta charset="utf-8">
<title>BRAVOK Cabinetry Inc. – Business Card</title>
<link rel="stylesheet" href="https://fonts.googleapis.com/css2?family=Cinzel:wght@400;700&family=Montserrat:wght@400;500&display=swap">
<style>
  :root {
    --backdrop: #e4e4e4;
    --card-white: #f7f7f6;
    --ink-grey: #5d5e60;
    --ink-dark: #2b2b2b;
    --accent: #e4552b;
    --band-grey: #55575a;
    --reverse-top: #67686b;
    --reverse-bottom: #3e3f41;
    --reverse-ink: #f4f4f4;
  }
  * { margin: 0; padding: 0; box-sizing: border-box; }
  html, body { width: 1200px; height: 720px; overflow: hidden; }
  body { background: var(--backdrop); position: relative; font-family: "Cinzel", serif; }

  .card {
    position: absolute; top: 223px; width: 480px; height: 274px;
    box-shadow: 0 18px 28px rgba(0,0,0,.28);
    overflow: hidden;
  }
  .card--front { left: 90px; background: var(--card-white); }
  .card--back {
    left: 630px;
    background: linear-gradient(135deg, var(--reverse-top), var(--reverse-bottom));
    display: flex; align-items: center; justify-content: center;
  }

  .brand { position: absolute; left: 30px; top: 24px; color: var(--ink-grey); }
  .brand__name {
    font-family: "Montserrat", sans-serif; font-weight: 400;
    font-size: 46px; line-height: 46px; letter-spacing: 4px; color: var(--ink-grey);
  }
  .brand__sub {
    font-family: "Montserrat", sans-serif; font-weight: 400;
    font-size: 14px; letter-spacing: 5.3px; color: var(--ink-grey); margin-top: 2px;
  }
  .brand__tagline {
    font-family: "Montserrat", sans-serif; font-weight: 500;
    font-size: 7.6px; letter-spacing: .8px; color: var(--accent); text-transform: uppercase;
  }

  .person { position: absolute; right: 31px; top: 110px; text-align: right; }
  .person__name { color: var(--accent); font-weight: 700; font-size: 15px; }
  .person__role { color: var(--ink-grey); font-size: 11px; margin-top: 1px; }

  .divider { position: absolute; left: 31px; right: 31px; top: 155px; height: 2px; background: var(--ink-grey); }

  .services {
    position: absolute; left: 31px; top: 163px; list-style: none;
    font-size: 9.6px; font-weight: 700; color: var(--ink-dark); line-height: 11.4px;
  }
  .services li::before {
    content: ""; display: inline-block; width: 4px; height: 4px; border-radius: 50%;
    background: var(--accent); margin-right: 5px; vertical-align: middle;
  }

  .contacts {
    position: absolute; right: 31px; top: 182px; list-style: none;
    text-align: right; font-size: 11px; color: var(--ink-dark); line-height: 14px;
  }
  .contacts li { display: flex; justify-content: flex-end; align-items: center; gap: 6px; }
  .contacts svg { width: 11px; height: 10px; flex: none; }

  .footer-band { position: absolute; left: 0; bottom: 0; width: 480px; height: 24px; }

  .brand--reverse { position: static; text-align: left; color: var(--reverse-ink); }
  .brand--reverse .brand__name { color: var(--reverse-ink); font-size: 62px; line-height: 62px; letter-spacing: 6px; }
  .brand--reverse .brand__sub { color: var(--reverse-ink); font-size: 18px; letter-spacing: 7.3px; }
  .brand--reverse .brand__tagline { color: var(--reverse-ink); font-size: 9.6px; font-weight: 400; letter-spacing: 1.6px; }
</style>
</head>
<body>
  <section class="card card--front" aria-label="Card front">
    <div class="brand">
      <div class="brand__name">BRAVOK</div>
      <div class="brand__sub">CABINETRY INC.</div>
      <div class="brand__tagline">Construction of interior solutions</div>
    </div>

    <div class="person">
      <div class="person__name">Dana Mercer</div>
      <div class="person__role">Manager</div>
    </div>

    <div class="divider"></div>

    <ul class="services">
      <li>Custom Kitchens</li>
      <li>Contemporary kitchens</li>
      <li>Traditional kitchens</li>
      <li>Vanities</li>
      <li>Libraries</li>
      <li>Custom Entry Doors</li>
      <li>Custom Wine Cellars</li>
      <li>Custom Design Furniture.</li>
    </ul>

    <ul class="contacts">
      <li>555-318-2746
        <svg viewBox="0 0 12 10" aria-hidden="true"><path d="M1 4 Q6 0 11 4 L10 5 L8 4 L8 3 Q6 2 4 3 L4 4 L2 5 Z M3 5 H9 L10 9 H2 Z" fill="var(--accent)"/></svg>
      </li>
      <li>BRAVOK@mailbox.example
        <svg viewBox="0 0 12 10" aria-hidden="true"><rect x="0.5" y="1" width="11" height="8" fill="var(--accent)"/><path d="M0.5 1 L6 5.5 L11.5 1" stroke="#fff" stroke-width="1" fill="none"/></svg>
      </li>
      <li>BRAVOKcabinetry.example
        <svg viewBox="0 0 12 10" aria-hidden="true"><rect x="0.8" y="0.8" width="10.4" height="6.6" fill="none" stroke="var(--accent)" stroke-width="1.4"/><rect x="4" y="8" width="4" height="1.6" fill="var(--accent)"/></svg>
      </li>
    </ul>

    <svg class="footer-band" viewBox="0 0 480 24" aria-hidden="true">
      <rect x="0" y="13" width="480" height="11" fill="var(--band-grey)"/>
      <polygon points="316,24 330,2 480,2 480,24" fill="var(--accent)"/>
      <polygon points="314,24 328,2 332,2 318,24" fill="var(--card-white)"/>
      <polygon points="335,24 349,2 354,2 340,24" fill="var(--card-white)"/>
    </svg>
  </section>

  <section class="card card--back" aria-label="Card back">
    <div class="brand brand--reverse">
      <div class="brand__name">BRAVOK</div>
      <div class="brand__sub">CABINETRY INC.</div>
      <div class="brand__tagline">Construction of interior solutions</div>
    </div>
  </section>
</body>
</html>
```